Harwick Legal

To update and modernize current business card appearance. Marta's business is based in Melbourne with 4 other lawyers in the firm. Marta travels to the Pilbara in Western Australia approximately 1 week a month as part of the firms legal work. She consults with clients in Newman, Tom Price and Port Hedland. The lawyers work mostly from a home office, apart from court appearances. They have a virtual office in Melbourne city, and use facilities in 3 or 4 other locations around Melbourne. It is important the client's think this is a conventional law firm with a permanent office. Our business structure is a difficult concept for them to grasp. The business has been operational for 3 years, growing from 1 lawyer to 4 lawyers during that time. Our website is www.Harwicklegal.example.au and is currently being upgraded as we are not happy with its content. The logo is currently orange and dark grey but the orange is a difficult colour to reproduce and often turns out "poo" brown when documents are printed. We need clients to know we are user friendly and caring - and not head up our rears ends as some lawyers appear to be.
Updates

Thank you for the feedback so far. 1. Some of the designs have too much black (We prefer darker grey & not too much.) 2. Happy for designers to play around with different colours & logo design. What we're after is a modern look and business card that people say "wow" when they pick it up.

Industry/Entity Type

Business

```html
<!DOCTYPE html>
<html lang="en">
<head>
<meta charset="utf-8">
<title>Harwick Legal – Business Card</title>
<link href="https://fonts.googleapis.com/css2?family=Arimo:wght@400;500&display=swap" rel="stylesheet">
<style>
  :root {
    --royal: #1a2f9e;
    --navy: #00006e;
    --sky: #3a8cff;
    --paper: #f4f4f4;
    --white: #ffffff;
    --ink-blue: #1a2f9e;
  }
  * { margin: 0; padding: 0; box-sizing: border-box; }
  html, body {
    width: 991px; height: 1200px; overflow: hidden;
    background: var(--white);
    font-family: "Arimo", Arial, sans-serif;
  }
  .canvas { position: relative; width: 991px; height: 1200px; }

  /* Front face */
  .brand-panel {
    position: absolute; left: 38px; top: 39px; width: 915px; height: 350px;
    background: radial-gradient(ellipse 75% 110% at 27% 95%, var(--sky) 0%, #2a5fd8 35%, #1c33b0 62%, var(--navy) 100%);
    display: flex; flex-direction: column; align-items: center; justify-content: center;
    color: var(--white);
  }
  .brand-mark {
    width: 120px; height: 120px; border-radius: 50%;
    border: 0; background: var(--white); opacity: .95;
    margin-bottom: 28px;
  }
  .brand-name {
    font-size: 62px; font-weight: 500; letter-spacing: 1px; line-height: 1;
  }
  .tagline-band {
    position: absolute; left: 38px; top: 407px; width: 915px; height: 157px;
    background: var(--royal); color: var(--white);
    display: flex; align-items: center; justify-content: center;
    font-size: 49px; font-weight: 500; letter-spacing: 1.5px;
  }

  /* Back face */
  .name-band {
    position: absolute; left: 38px; top: 626px; width: 915px; height: 188px;
    background: var(--royal); color: var(--white); text-align: center;
  }
  .person-name { margin-top: 28px; font-size: 66px; font-weight: 500; letter-spacing: 1px; line-height: 1; }
  .credentials { margin-top: 30px; font-size: 19px; }

  .details {
    position: absolute; left: 38px; top: 814px; width: 915px; height: 220px;
    background: var(--paper); color: var(--ink-blue);
  }
  .practice { position: absolute; left: 24px; top: 14px; }
  .practice-title {
    font-size: 22px; display: inline-block;
    border-bottom: 1.5px solid var(--ink-blue); padding-bottom: 2px; margin-bottom: 14px;
  }
  .practice-area { font-size: 22px; line-height: 1.3; }
  .practice-sub { font-size: 15px; padding-left: 21px; line-height: 31px; }
  .practice-sub:first-of-type { margin-top: 2px; }

  .contact { position: absolute; right: 20px; top: 17px; text-align: right; }
  .role { font-size: 30px; margin-bottom: 20px; }
  .contact-line { font-size: 26px; line-height: 45px; }

  .divider-band {
    position: absolute; left: 38px; top: 1034px; width: 915px; height: 17px;
    background: var(--royal);
  }
  .values-band {
    position: absolute; left: 38px; top: 1051px; width: 915px; height: 100px;
    background: var(--paper); color: var(--ink-blue);
    display: flex; align-items: center; justify-content: space-around;
    padding: 0 50px 0 64px; font-size: 40px;
  }
</style>
</head>
<body>
<main class="canvas">
  <section class="brand-panel">
    <div class="brand-mark" aria-hidden="true"></div>
    <div class="brand-name">Harwick Legal</div>
  </section>
  <section class="tagline-band">Serving The People Of The Pilbara</section>

  <section class="name-band">
    <h1 class="person-name">J. Marta Quinlan</h1>
    <p class="credentials">LLB (Hons), Dip Pro Mgt - Accredited Mediator</p>
  </section>

  <section class="details">
    <div class="practice">
      <div class="practice-title">Areas of Practice:</div>
      <div class="practice-area">-Family Law</div>
      <div class="practice-sub">Collaboratice Practice</div>
      <div class="practice-sub">Meditation &amp; Negotiation</div>
      <div class="practice-sub">Intervention Orders</div>
      <div class="practice-area">-Criminal Law</div>
    </div>
    <div class="contact">
      <div class="role">Principal Solicitor</div>
      <div class="contact-line">t: 1300 HARWICK (1300 427 942)</div>
      <div class="contact-line">m: 0400 555 018</div>
      <div class="contact-line">e: marta.quinlan@harwicklegal.example.au</div>
    </div>
  </section>

  <div class="divider-band"></div>
  <section class="values-band">
    <span>Experience</span><span>-</span><span>Support</span><span>-</span><span>Solutions</span>
  </section>
</main>
</body>
</html>
```